Kit Layout de Posts para Redes Sociais (Facebook, Instagram e etc)para Dra Marcela Toledano
Postado por: marcelatoledano_5830174416   Estou Offline
Projeto para criar:
Kit Layout de Posts para Redes Sociais (Facebook, Instagram e etc)
Clientes com PC preferem arquivos em CorelDraw (CDR).
Imagem: Imagem JPG (alta resoluçao) PNG em camadas PSD em camadas PDF Sem Preferência Tipos possíveis: Imagem JPG (alta resoluçao), PNG em camadas, PSD em camadas, PDF.

```html
<!DOCTYPE html>
<html lang="pt-BR">
<head>
<meta charset="UTF-8">
<title>Dra. Marcela Toledano – Post</title>
<link rel="stylesheet" href="https://fonts.googleapis.com/css2?family=Lato:wght@400;700;900&display=swap">
<style>
  :root {
    --plum-deep: #4f2640;
    --plum: #6b3a58;
    --mauve: #9a7088;
    --mauve-soft: #c7a8b6;
    --skin-light: #ead5cf;
    --skin: #d9b6ad;
    --skin-shadow: #b98f8c;
    --gold: #c9a063;
    --white: #ffffff;
  }
  * { margin: 0; padding: 0; box-sizing: border-box; }
  html, body { width: 1200px; height: 1200px; overflow: hidden; }
  body { font-family: "Lato", Arial, sans-serif; background: var(--plum-deep); }
  .post { position: relative; width: 1200px; height: 1200px; overflow: hidden; }
  .backdrop {
    position: absolute; inset: 0;
    background: linear-gradient(90deg, var(--mauve) 0%, var(--mauve-soft) 35%, #dcc4c6 60%, #e0c9c4 100%);
  }
  .hero-photo {
    position: absolute; left: 300px; top: 0; width: 900px; height: 1060px;
    background:
      radial-gradient(ellipse 420px 560px at 70% 50%, var(--skin-light) 0%, var(--skin) 60%, rgba(217,182,173,0) 100%),
      linear-gradient(90deg, rgba(220,196,198,0) 0%, var(--skin) 45%, var(--skin-shadow) 100%);
  }
  .headline {
    position: absolute; left: 72px; top: 148px;
    color: var(--plum);
    font-weight: 900; font-size: 76px; line-height: 1.0;
    letter-spacing: 1px; text-transform: uppercase;
  }
  .intro {
    position: absolute; left: 72px; top: 394px; width: 490px;
    color: var(--white);
    font-weight: 700; font-size: 25px; line-height: 1.42;
    letter-spacing: 0.3px;
  }
  .footer-band { position: absolute; left: 0; top: 0; width: 1200px; height: 1200px; }
  .contact { position: absolute; color: var(--white); font-size: 30px; letter-spacing: 0.8px; }
  .contact-web { top: 1068px; left: 196px; }
  .contact-row { top: 1124px; left: 96px; display: flex; align-items: center; gap: 34px; }
  .contact-item { display: flex; align-items: center; gap: 10px; }
  .icon-dot { width: 30px; height: 30px; border: 3px solid var(--white); border-radius: 50%; }
  .brand {
    position: absolute; right: 52px; top: 1046px;
    display: flex; align-items: center; gap: 14px;
  }
  .brand-mark { width: 60px; height: 60px; border: 3px solid var(--gold); border-radius: 50%; }
  .brand-name { color: var(--gold); font-weight: 700; font-size: 36px; line-height: 1.1; }
</style>
</head>
<body>
<main class="post">
  <div class="backdrop"></div>
  <div class="hero-photo" role="img" aria-label="Foto: mão com luva branca marcando com caneta cirúrgica o abdômen de uma paciente para cirurgia plástica"></div>

  <h1 class="headline">Lorem<br>Ipsum dolor<br>sit amet</h1>
  <p class="intro">Lorem ipsum dolor sit amet, consectetur adipiscing elit, sed do eiusmod tempor incididunt</p>

  <svg class="footer-band" viewBox="0 0 1200 1200" aria-hidden="true">
    <path d="M0 1000 C430 985 900 910 1200 720 L1200 1200 L0 1200 Z" fill="#8a5a74" opacity="0.5"/>
    <path d="M0 1040 C430 1020 900 950 1200 760 L1200 1200 L0 1200 Z" fill="var(--plum-deep)"/>
    <path d="M0 1036 C430 1016 900 946 1200 756" fill="none" stroke="var(--gold)" stroke-width="6"/>
  </svg>

  <p class="contact contact-web">www.marcelatoledano.com.br</p>
  <div class="contact contact-row">
    <span class="contact-item">
      <svg width="30" height="30" viewBox="0 0 24 24" aria-hidden="true"><path d="M6.6 10.8a15 15 0 0 0 6.6 6.6l2.2-2.2a1 1 0 0 1 1-.25 11.4 11.4 0 0 0 3.6.57 1 1 0 0 1 1 1V20a1 1 0 0 1-1 1A17 17 0 0 1 3 4a1 1 0 0 1 1-1h3.5a1 1 0 0 1 1 1c0 1.25.2 2.45.57 3.6a1 1 0 0 1-.25 1z" fill="#fff"/></svg>
      47 98250-3174
    </span>
    <span class="contact-item"><span class="icon-dot"></span>/marcelatoledano</span>
  </div>

  <div class="brand">
    <span class="brand-mark"></span>
    <span class="brand-name">Dra. Marcela<br>Toledano</span>
  </div>
</main>
</body>
</html>
```